Proposal Template Design

We are looking to have our proposal templates redesigned. attached are examples of what we have been using. as well as our current logo

```html
<!DOCTYPE html>
<html lang="en">
<head>
<meta charset="utf-8">
<title>Northline Insulation Letterhead</title>
<link rel="stylesheet" href="https://fonts.googleapis.com/css2?family=Barlow:wght@500;600;700&display=swap">
<style>
  :root {
    --backdrop: #b4ccd5;
    --paper: #ffffff;
    --navy: #0c1a33;
    --royal: #1550b8;
    --sky: #1fa3e0;
    --ink-light: #ffffff;
    --brand: #123f9a;
  }
  * { margin: 0; padding: 0; box-sizing: border-box; }
  html, body {
    width: 1200px; height: 1200px; overflow: hidden;
    background: var(--backdrop);
    font-family: "Barlow", Arial, sans-serif;
  }
  .letterhead {
    position: absolute; left: 175px; top: 50px;
    width: 850px; height: 1100px;
    background: var(--paper);
    box-shadow: 0 12px 30px rgba(20, 45, 60, 0.25);
    overflow: hidden;
  }
  .header-waves, .footer-waves { position: absolute; left: 0; width: 850px; display: block; }
  .header-waves { top: 0; height: 180px; }
  .footer-waves { bottom: 0; height: 130px; }
  .services {
    position: absolute; top: 40px; right: 40px;
    display: flex; gap: 14px; align-items: center;
    color: var(--ink-light); font-size: 12px; font-weight: 500;
    letter-spacing: 0.3px; text-transform: uppercase;
  }
  .services .divider { opacity: 0.8; }
  .brand {
    position: absolute; top: 62px; left: 52px;
    display: flex; align-items: center; gap: 10px;
  }
  .brand-square { width: 26px; height: 26px; background: var(--brand); }
  .brand-name {
    color: var(--brand); font-size: 22px; font-weight: 700; line-height: 1;
  }
  .contact {
    position: absolute; display: flex; align-items: center; gap: 8px;
    color: var(--ink-light); font-size: 14px; font-weight: 500;
  }
  .contact svg { width: 16px; height: 16px; flex: none; }
  .contact-address { left: 40px; bottom: 26px; }
  .contact-email { left: 400px; bottom: 50px; }
  .contact-phone { left: 680px; bottom: 78px; }
</style>
</head>
<body>
  <main class="letterhead">
    <svg class="header-waves" viewBox="0 0 850 180" preserveAspectRatio="none" aria-hidden="true">
      <path fill="var(--sky)" d="M0,0 H850 V90 C820,88 770,92 700,110 C600,135 500,135 420,100 C300,40 150,30 0,40 Z"/>
      <path fill="var(--royal)" d="M240,0 H850 V75 C830,75 790,80 720,98 C640,120 540,120 470,90 C400,50 330,20 240,0 Z"/>
      <path fill="var(--navy)" d="M300,0 H850 V58 C830,58 790,62 720,80 C640,100 560,100 500,80 C440,55 380,25 300,0 Z"/>
    </svg>

    <nav class="services">
      <span>Spray Foam</span><span class="divider">|</span>
      <span>Fiberglass</span><span class="divider">|</span>
      <span>Insulation</span><span class="divider">|</span>
      <span>Roofing</span>
    </nav>

    <div class="brand">
      <span class="brand-square"></span>
      <span class="brand-name">Northline Insulation</span>
    </div>

    <svg class="footer-waves" viewBox="0 0 850 130" preserveAspectRatio="none" aria-hidden="true">
      <path fill="var(--royal)" d="M0,130 V100 C200,72 350,48 500,46 C650,44 760,22 850,0 V130 Z"/>
      <path fill="var(--sky)" d="M0,130 V58 C120,42 260,42 380,76 C430,90 460,110 480,130 Z"/>
    </svg>

    <div class="contact contact-address">
      <svg viewBox="0 0 16 16" fill="none" stroke="currentColor" stroke-width="1.4"><circle cx="8" cy="8" r="7"/><path d="M8 12.5 C6 10 5.3 8.8 5.3 7.4 a2.7 2.7 0 0 1 5.4 0 C10.7 8.8 10 10 8 12.5 Z"/></svg>
      <span>P.O Box 218, Fairview Ridge 70412</span>
    </div>
    <div class="contact contact-email">
      <svg viewBox="0 0 16 16" fill="none" stroke="currentColor" stroke-width="1.4"><circle cx="8" cy="8" r="7"/><rect x="4.5" y="5.5" width="7" height="5" fill="currentColor" stroke="none"/></svg>
      <span>office@northlineinsul.com</span>
    </div>
    <div class="contact contact-phone">
      <svg viewBox="0 0 16 16" fill="none" stroke="currentColor" stroke-width="1.4"><circle cx="8" cy="8" r="7"/><path d="M5.4 4.8 l1.3 -0.3 0.8 1.8 -0.9 0.7 c0.5 1 1.2 1.7 2.2 2.2 l0.7 -0.9 1.8 0.8 -0.3 1.3 C8 10.6 5.4 8 5.4 4.8 Z" fill="currentColor" stroke="none"/></svg>
      <span>555-014-2290</span>
    </div>
  </main>
</body>
</html>
```